New Business Card Design Project

Bloom of the Willow Wellness Clinic PLLC
Bloomofthewillowwc-example.com
Board Certified Nursing Coach in life, health, & wellness.
Hypnotherapy, weight loss & vitamin supplement injections, IV hydration.
Offering mobile clinics

```html
<!DOCTYPE html>
<html lang="en">
<head>
<meta charset="utf-8">
<title>Bloom of the Willow Wellness Clinic – Business Cards</title>
<link rel="stylesheet" href="https://fonts.googleapis.com/css2?family=Lato:wght@400;700&display=swap">
<style>
  :root {
    --backdrop: #9a9a9a;
    --card: #5c2e32;
    --accent: #f0821e;
    --cream: #f6eedc;
    --text: #f4eded;
    --rule: #e9dede;
  }
  * { margin: 0; padding: 0; box-sizing: border-box; }
  html, body { width: 1200px; height: 1108px; overflow: hidden; }
  body {
    background: var(--backdrop);
    font-family: "Lato", sans-serif;
    position: relative;
    color: var(--text);
  }
  .card {
    position: absolute;
    background: var(--card);
    border-radius: 27px;
  }
  .card--front { left: 234px; top: 117px; width: 744px; height: 424px; }
  .card--back  { left: 234px; top: 580px; width: 730px; height: 416px; }

  .brand { position: absolute; display: flex; align-items: center; }
  .card--front .brand { left: 60px; top: 100px; }
  .card--back .brand  { left: 57px; top: 52px; }
  .brand__mark {
    width: 100px; height: 100px; border-radius: 50%;
    background: var(--accent); flex: none;
  }
  .brand__name {
    margin-left: 24px;
    font-weight: 700; color: var(--cream);
    text-transform: uppercase;
  }
  .brand__title { display: block; font-size: 37px; letter-spacing: 2px; line-height: 1.1; }
  .brand__sub { display: block; font-size: 22px; letter-spacing: 5px; margin-top: 10px; text-align: center; }

  .services {
    position: absolute; left: 0; right: 0; top: 322px;
    text-align: center; font-size: 20px; line-height: 25px;
  }

  .person { position: absolute; left: 41px; top: 222px; }
  .person__name { font-size: 31px; font-weight: 700; color: var(--accent); letter-spacing: -0.3px; line-height: 1; }
  .person__role { font-size: 20px; margin-top: 10px; }

  .divider {
    position: absolute; left: 46px; top: 296px; width: 636px;
    height: 2px; background: var(--rule);
  }

  .contacts { position: absolute; left: 41px; top: 309px; list-style: none; }
  .contacts li { display: flex; align-items: center; font-size: 20px; height: 27px; }
  .contacts li + li { margin-top: 2px; }
  .contacts svg { width: 22px; height: 22px; fill: var(--accent); margin-right: 16px; flex: none; }

  .address {
    position: absolute; right: 51px; top: 337px;
    text-align: right; font-size: 20px; line-height: 28px; font-style: normal;
  }
</style>
</head>
<body>

<section class="card card--front">
  <div class="brand">
    <span class="brand__mark"></span>
    <span class="brand__name">
      <span class="brand__title">Bloom of the Willow</span>
      <span class="brand__sub">Wellness Clinic</span>
    </span>
  </div>
  <p class="services">Hypnotherapy, Weight loss &amp; Vitamin Supplement Injections,<br>IV hydration. Offering mobile clinics</p>
</section>

<section class="card card--back">
  <div class="brand">
    <span class="brand__mark"></span>
    <span class="brand__name">
      <span class="brand__title">Bloom of the Willow</span>
      <span class="brand__sub">Wellness Clinic</span>
    </span>
  </div>

  <div class="person">
    <h1 class="person__name">DANIEL HARPER</h1>
    <p class="person__role">Board Certified Nursing Coach in life, health, &amp; wellness.</p>
  </div>

  <div class="divider"></div>

  <ul class="contacts">
    <li>
      <svg viewBox="0 0 24 24" aria-hidden="true"><path d="M6.6 10.8a15.1 15.1 0 0 0 6.6 6.6l2.2-2.2a1 1 0 0 1 1-.25 11.4 11.4 0 0 0 3.6.57 1 1 0 0 1 1 1V20a1 1 0 0 1-1 1A17 17 0 0 1 3 4a1 1 0 0 1 1-1h3.5a1 1 0 0 1 1 1c0 1.25.2 2.45.57 3.57a1 1 0 0 1-.25 1z"/></svg>
      044-555 010 247
    </li>
    <li>
      <svg viewBox="0 0 24 24" aria-hidden="true"><path d="M2 5h20v14H2z" opacity="0"/><path d="M2 5h20v2l-10 6L2 7z"/><path d="M2 9l10 6 10-6v10H2z"/></svg>
      info@bloomwillow-example.com
    </li>
    <li>
      <svg viewBox="0 0 24 24" aria-hidden="true"><path d="M12 2a10 10 0 1 0 0 20 10 10 0 0 0 0-20zm-1 17.9A8 8 0 0 1 4.2 10.2L9 15v1a2 2 0 0 0 2 2zm6.9-2.5A2 2 0 0 0 16 16h-1v-3a1 1 0 0 0-1-1H8v-2h2a1 1 0 0 0 1-1V7h2a2 2 0 0 0 2-2v-.4a8 8 0 0 1 2.9 12.8z"/></svg>
      www.Bloomofthewillowwc-example.com
    </li>
  </ul>

  <address class="address">421, Address line goes here<br>45452, Country name</address>
</section>

</body>
</html>
```